Refrigeration & Air Conditioning modern and appealing

We want to design a business card that is modern and appealing using existing logo supplied

Front card
Residential Commercial Diary
RTA : AU052731
Licence L287456

Back card
Warren Kostig
Director
0491 357 208
info@frostlinerefrigeration.com.au
www.frostlinerefrigeration.com.au
• Air Conditioning
• Cool Rooms & Refrigeration
• Installation
• Service & Repair
• Preventative Maintenance

We offer 24/7 emergency service

```html
<!DOCTYPE html>
<html lang="en">
<head>
<meta charset="utf-8">
<title>Frostline Business Card</title>
<link rel="stylesheet" href="https://fonts.googleapis.com/css2?family=Roboto:wght@400;500;700;900&display=swap">
<style>
  :root {
    --bg: #1a1a1c;
    --card: #242426;
    --card-dark: #1d1d1f;
    --purple: #b14ef0;
    --purple-deep: #7b3fe0;
    --purple-light: #d07cf7;
    --white: #ffffff;
    --muted: #e6e3ea;
  }
  * { margin: 0; padding: 0; box-sizing: border-box; }
  html, body { width: 1200px; height: 840px; overflow: hidden; }
  body {
    background: var(--bg);
    font-family: "Roboto", Arial, sans-serif;
    color: var(--white);
    display: flex;
    flex-direction: column;
    align-items: center;
    justify-content: center;
    gap: 40px;
  }
  .card {
    position: relative;
    width: 640px;
    height: 366px;
    border-radius: 26px;
    background: linear-gradient(135deg, var(--card) 0%, var(--card-dark) 100%);
    box-shadow: -3px 4px 0 var(--purple), 0 18px 40px rgba(0,0,0,.55);
    overflow: hidden;
  }

  /* Front */
  .brand {
    display: flex;
    align-items: center;
    gap: 14px;
  }
  .brand-dot {
    border-radius: 50%;
    background: linear-gradient(135deg, var(--purple-light), var(--purple-deep));
  }
  .brand-name {
    font-weight: 900;
    color: var(--white);
    letter-spacing: 2px;
    text-transform: uppercase;
  }
  .card-front .brand { position: absolute; left: 92px; top: 58px; }
  .card-front .brand-dot { width: 70px; height: 70px; }
  .card-front .brand-name { font-size: 52px; }

  .sector-band {
    position: absolute;
    left: 40px; right: 40px; top: 160px;
    height: 40px;
    background: linear-gradient(90deg, rgba(123,63,224,0) 0%, var(--purple-deep) 20%, var(--purple) 75%, rgba(177,78,240,0) 100%);
    display: flex;
    align-items: center;
    justify-content: center;
    gap: 26px;
    font-weight: 700;
    font-size: 20px;
  }

  .services {
    position: absolute;
    left: 0; right: 0; top: 222px;
    text-align: center;
    font-size: 19px;
    line-height: 30px;
    color: var(--muted);
  }
  .services li { display: inline; list-style: none; }
  .services li::before {
    content: "";
    display: inline-block;
    width: 9px; height: 9px;
    border-radius: 50%;
    background: var(--purple);
    margin: 0 7px 2px 12px;
  }

  /* Back */
  .card-back .brand { position: absolute; left: 70px; top: 160px; }
  .card-back .brand-dot { width: 46px; height: 46px; }
  .card-back .brand-name { font-size: 32px; }

  .divider {
    position: absolute;
    left: 330px; top: 60px;
    width: 1.5px; height: 170px;
    background: var(--muted);
  }
  .contact {
    position: absolute;
    left: 352px; top: 62px;
  }
  .contact-name {
    font-weight: 700;
    font-size: 24px;
    color: var(--purple);
    text-transform: uppercase;
    letter-spacing: .5px;
  }
  .contact-role { font-size: 17px; margin-top: 2px; }
  .contact-list { list-style: none; margin-top: 22px; }
  .contact-list li {
    display: flex; align-items: center; gap: 8px;
    font-size: 15px; line-height: 24px;
  }
  .contact-list svg { width: 15px; height: 15px; fill: var(--purple); flex: none; }

  .emergency-tab {
    position: absolute;
    right: 0; bottom: 0;
    width: 420px; height: 66px;
  }
  .emergency-tab svg { position: absolute; inset: 0; }
  .emergency-text {
    position: absolute;
    inset: 18px 0 0 40px;
    display: flex; align-items: center; justify-content: center;
    font-size: 21px;
  }
</style>
</head>
<body>

  <section class="card card-front">
    <div class="brand">
      <span class="brand-dot"></span>
      <span class="brand-name">Frostline</span>
    </div>
    <div class="sector-band">
      <span>Residential</span><span>Commercial</span><span>Diary</span>
    </div>
    <ul class="services">
      <li>Air Conditioning</li><li>Refrigeration</li><br>
      <li>Cool / Freezer Rooms</li><li>Ice Machines</li><br>
      <li>Installation</li><li>Service &amp; Repair</li><li>Preventative Maintenance</li>
    </ul>
  </section>

  <section class="card card-back">
    <div class="brand">
      <span class="brand-dot"></span>
      <span class="brand-name">Frostline</span>
    </div>
    <div class="divider"></div>
    <div class="contact">
      <div class="contact-name">Warren Kostig</div>
      <div class="contact-role">Director</div>
      <ul class="contact-list">
        <li>
          <svg viewBox="0 0 24 24" aria-hidden="true"><path d="M6.6 10.8a15.1 15.1 0 0 0 6.6 6.6l2.2-2.2c.3-.3.7-.4 1-.2 1.1.4 2.3.6 3.6.6.6 0 1 .4 1 1V20c0 .6-.4 1-1 1A17 17 0 0 1 3 4c0-.6.4-1 1-1h3.5c.6 0 1 .4 1 1 0 1.3.2 2.5.6 3.6.1.3 0 .7-.2 1z"/></svg>
          0491 357 208
        </li>
        <li>
          <svg viewBox="0 0 24 24" aria-hidden="true"><path d="M3 5h18v14H3zm2 2v.5l7 4.5 7-4.5V7zm0 2.9V17h14V9.9l-7 4.5z"/></svg>
          info@frostlinerefrigeration.com.au
        </li>
        <li>
          <svg viewBox="0 0 24 24" aria-hidden="true"><path d="M12 2a10 10 0 1 0 0 20 10 10 0 0 0 0-20zm6.9 6h-3a15.7 15.7 0 0 0-1.4-3.6A8 8 0 0 1 18.9 8zM12 4c.8 1.2 1.5 2.5 1.9 4h-3.8c.4-1.4 1.1-2.8 1.9-4zM4.3 14a8.2 8.2 0 0 1 0-4h3.4a16.5 16.5 0 0 0 0 4zm.8 2h3c.3 1.3.8 2.5 1.4 3.6A8 8 0 0 1 5.1 16zm3-8h-3a8 8 0 0 1 4.4-3.6C8.9 5.5 8.4 6.7 8.1 8zM12 20c-.8-1.2-1.5-2.5-1.9-4h3.8c-.4 1.4-1.1 2.8-1.9 4zm2.3-6H9.7a14.7 14.7 0 0 1 0-4h4.6a14.7 14.7 0 0 1 0 4zm.2 5.6c.6-1.1 1.1-2.3 1.4-3.6h3a8 8 0 0 1-4.4 3.6zm1.8-5.6a16.5 16.5 0 0 0 0-4h3.4a8.2 8.2 0 0 1 0 4z"/></svg>
          www.frostlinerefrigeration.com.au
        </li>
      </ul>
    </div>
    <div class="emergency-tab">
      <svg viewBox="0 0 420 66" preserveAspectRatio="none" aria-hidden="true">
        <defs>
          <linearGradient id="tabFill" x1="0" x2="1" y1="0" y2="0">
            <stop offset="0" stop-color="#c24ef2"/>
            <stop offset="1" stop-color="#9a48e6"/>
          </linearGradient>
        </defs>
        <path d="M0 66 C20 66 22 18 50 18 L340 18 C370 18 370 0 395 0 L420 0 L420 66 Z" fill="url(#tabFill)"/>
      </svg>
      <div class="emergency-text">We offer 24/7 emergency service</div>
    </div>
  </section>

</body>
</html>
```